Business Card for Coach - ready to print

Design Business Card ready to order prints www.lukasbrenner.coach

* An Overview / Background of the Business & Services
· Coaching
· Personal growth
* The Target Market / Audience you are trying to reach
· private person in different roles (self, familiy, business role)s
* Design Specifics; any preferences or ideas for Style, Colour, Imagery, etc
· See www.lukasbrenner.coach
· "simple" design
· (small) element of surprise / unusual element

* Information that will be placed in the Business Card
· Beratung und Coaching
· Address: Lukas Brenner, Talmatt 42, CH-8531 Winterthur, Mobile +41 76 254 63 07
* Do you have an existing website or Facebook page where designers can learn more about your company?
· lukasbrenner.coach

Target Market(s)

private person in different roles (self, familiy, business role)

Industry/Entity Type

Life Coaching

Contact Information for Business Card

Lukas Brenner
Talmatt 42
CH-8531 Winterthur

Mobile: +41 76 254 63 07
Email: lubr@sonnwelt.ch
www.lukasbrenner.coach

Font styles to use
Sans Serif

Colors

Designer to choose colors to be used in the design.

Requirements
Must have
• "simple" design
• element of surprise / unusual element
• Beratung & Coaching
• see www.lukasbrenner.coach for colors and so...
Nice to have
• TA Symbol (three rings on top of each other) - unsual presentation
• QR Code of Website (see if it fits in and still looks good).

```html
<!DOCTYPE html>
<html lang="de">
<head>
<meta charset="utf-8">
<title>Lukas Brenner – Visitenkarte</title>
<link rel="stylesheet" href="https://fonts.googleapis.com/css2?family=Roboto:wght@400;700&display=swap">
<style>
  :root {
    --page: #e6e6e6;
    --sky: #86b8d3;
    --sky-light: #9cc6dc;
    --sky-wash: #93bfa9;
    --ink: #676b6e;
    --amber: #dea534;
    --amber-light: #e3ae43;
    --wood: #d9ab55;
    --wood-block: #c9a878;
    --white: #ffffff;
  }
  * { box-sizing: border-box; margin: 0; padding: 0; }
  html, body { width: 1200px; height: 857px; overflow: hidden; }
  body {
    background: var(--page);
    font-family: "Roboto", Arial, sans-serif;
    display: flex;
    align-items: center;
    justify-content: center;
    gap: 40px;
  }
  .card {
    position: relative;
    width: 520px;
    height: 336px;
    overflow: hidden;
    box-shadow: 0 6px 18px rgba(0,0,0,0.12);
  }
  .card-texture { position: absolute; inset: 0; }

  /* Front */
  .card-front .card-texture {
    background:
      radial-gradient(ellipse at 25% 60%, rgba(147,191,169,0.45), transparent 55%),
      radial-gradient(ellipse at 75% 30%, rgba(147,191,169,0.35), transparent 50%),
      linear-gradient(160deg, var(--sky-light), var(--sky));
  }
  .brand {
    position: absolute;
    left: 190px;
    top: 118px;
    color: var(--ink);
    font-weight: 700;
  }
  .brand-name {
    font-size: 30px;
    line-height: 1.1;
    padding-bottom: 3px;
    border-bottom: 2px solid var(--ink);
  }
  .brand-tagline {
    font-size: 17px;
    margin-top: 4px;
  }

  /* Back */
  .card-back { background: var(--amber); }
  .card-back .card-texture {
    left: auto;
    width: 44%;
    background: radial-gradient(ellipse at 65% 45%, var(--wood) 0%, var(--amber-light) 45%, var(--amber) 75%);
  }
  .contact-list {
    position: absolute;
    left: 96px;
    top: 140px;
    list-style: none;
  }
  .contact-item {
    display: flex;
    align-items: center;
    gap: 20px;
    height: 38px;
  }
  .contact-icon {
    width: 30px;
    height: 30px;
    background: var(--wood-block);
    display: flex;
    align-items: center;
    justify-content: center;
    flex: none;
  }
  .contact-icon svg { width: 18px; height: 18px; }
  .contact-text {
    color: var(--white);
    font-size: 17px;
    letter-spacing: 0.3px;
  }
</style>
</head>
<body>
  <section class="card card-front" aria-label="Vorderseite">
    <div class="card-texture" role="img" aria-label="Holzklötze, hellblau lasiert"></div>
    <div class="brand">
      <p class="brand-name">Lukas Brenner</p>
      <p class="brand-tagline">Beratung &amp; Coaching</p>
    </div>
  </section>

  <section class="card card-back" aria-label="Rückseite">
    <div class="card-texture" role="img" aria-label="Natürliche Holzklötze in warmem Gelb"></div>
    <ul class="contact-list">
      <li class="contact-item">
        <span class="contact-icon">
          <svg viewBox="0 0 24 24" fill="none" stroke="#fff" stroke-width="2.2" stroke-linejoin="round"><path d="M3 11 L12 3 L21 11 V21 H3 Z"/><circle cx="12" cy="13" r="3"/></svg>
        </span>
        <span class="contact-text">Talmatt 42, CH-8531 Winterthur</span>
      </li>
      <li class="contact-item">
        <span class="contact-icon">
          <svg viewBox="0 0 24 24" fill="#fff"><path d="M6.6 10.8a15 15 0 0 0 6.6 6.6l2.2-2.2c.3-.3.7-.4 1-.2 1.1.4 2.3.6 3.6.6.6 0 1 .4 1 1V20c0 .6-.4 1-1 1A17 17 0 0 1 3 4c0-.6.4-1 1-1h3.5c.6 0 1 .4 1 1 0 1.3.2 2.5.6 3.6.1.3 0 .7-.2 1z"/></svg>
        </span>
        <span class="contact-text">+41 76 254 63 07</span>
      </li>
      <li class="contact-item">
        <span class="contact-icon">
          <svg viewBox="0 0 24 24" fill="none" stroke="#fff" stroke-width="2.2" stroke-linejoin="round"><rect x="3" y="6" width="18" height="12"/><path d="M3 6 L12 13 L21 6"/></svg>
        </span>
        <span class="contact-text">lubr@sonnwelt.ch</span>
      </li>
      <li class="contact-item">
        <span class="contact-icon">
          <svg viewBox="0 0 24 24" fill="none" stroke="#fff" stroke-width="2"><circle cx="12" cy="12" r="9"/><ellipse cx="12" cy="12" rx="4" ry="9"/><path d="M3 12 H21"/></svg>
        </span>
        <span class="contact-text">www.lukasbrenner.coach</span>
      </li>
    </ul>
  </section>
</body>
</html>
```